Life Coach for Lawyers Business Card Design

Elegant, original, business card design for life coaching service for associate attorneys who work in big law and struggle with stress, overwhelm, and time management. Double sided design.

Target Market(s)

Women associate attorneys who work in big law and struggle with stress, overwhelm, and time management.

Industry/Entity Type

Life Coaching

Contact Information for Business Card

Marissa Pendrell
Life Coach
518.677.3941
calmbriefcounsel.net
marissa@calmbriefcounsel.net
@calmbriefcounsel (Instagram)

Font styles to use
Other font styles liked:
• Silver South font duo. See uploaded files.

Requirements
Must have
• Icons for phone, website, email, and Instagram instead of words. Specific colors used in my logo (171B2B, 421121, FFFFFF)
Nice to have
• Foil. Embossed. Feminine design.
Should not have
• Any colors other than those used in logo. See uploaded files.

```html
<!DOCTYPE html>
<html lang="en">
<head>
<meta charset="UTF-8">
<title>Calm Brief Counsel – Business Card</title>
<link href="https://fonts.googleapis.com/css2?family=Playfair+Display:wght@500&family=Delius&family=Roboto+Slab:wght@700&family=Tinos&display=swap" rel="stylesheet">
<style>
  :root {
    --ink: #171B2B;
    --wine: #421121;
    --white: #FFFFFF;
    --page: #FFFFFF;
    --blush: #e8d3c8;
    --rose: #e3cfd3;
    --cream: #f8f4e2;
    --butter: #f6f1c8;
    --mint: #f3f6ee;
  }
  * { box-sizing: border-box; margin: 0; padding: 0; }
  html, body { width: 1200px; height: 1200px; overflow: hidden; background: var(--page); }
  .sheet {
    width: 1200px; height: 1200px;
    display: flex; flex-direction: column; align-items: center; justify-content: center;
    gap: 36px;
  }
  .card {
    position: relative;
    width: 960px; height: 549px;
    overflow: hidden;
    box-shadow: 0 2px 6px rgba(66,17,33,0.25);
    background:
      radial-gradient(ellipse 60% 55% at 45% 75%, var(--butter) 0%, rgba(246,241,200,0) 70%),
      radial-gradient(ellipse 45% 45% at 15% 25%, rgba(255,255,255,0.55) 0%, rgba(255,255,255,0) 70%),
      radial-gradient(ellipse 50% 60% at 95% 40%, var(--rose) 0%, rgba(227,207,211,0) 70%),
      linear-gradient(175deg, var(--blush) 0%, var(--cream) 50%, var(--mint) 100%);
  }
  .card--front { display: flex; align-items: center; justify-content: center; }
  .brand-name {
    font-family: "Playfair Display", Georgia, serif;
    font-weight: 500;
    color: var(--wine);
    text-align: center;
    line-height: 1.02;
    letter-spacing: 0.02em;
    text-transform: uppercase;
  }
  .brand-name .line-small { display: block; font-size: 64px; letter-spacing: 0.12em; }
  .brand-name .line-large { display: block; font-size: 132px; }

  .card--back { padding: 0 70px; }
  .holder-name {
    position: absolute; top: 150px; left: 0; right: 0;
    text-align: center;
    font-family: "Delius", "Comic Sans MS", cursive;
    font-size: 64px; color: var(--ink); letter-spacing: 0.02em;
  }
  .holder-role {
    position: absolute; top: 245px; left: 0; right: 0;
    text-align: center;
    font-family: "Roboto Slab", Georgia, serif;
    font-weight: 700; font-size: 30px; color: var(--wine);
  }
  .contact-grid {
    position: absolute; top: 390px; left: 70px; right: 70px;
    display: grid; grid-template-columns: 1fr 1.15fr; row-gap: 22px; column-gap: 40px;
    list-style: none;
  }
  .contact-item {
    display: flex; align-items: center; gap: 18px;
    font-family: "Tinos", "Times New Roman", serif;
    font-size: 23px; color: var(--ink);
  }
  .contact-item svg { width: 24px; height: 24px; flex: none; }
  .contact-item:nth-child(2) { padding-left: 22px; }
  .contact-item:nth-child(4) { padding-left: 22px; }
</style>
</head>
<body>
<main class="sheet">
  <section class="card card--front" aria-label="Card front">
    <h1 class="brand-name">
      <span class="line-small">Calm Brief</span>
      <span class="line-large">Counsel</span>
    </h1>
  </section>

  <section class="card card--back" aria-label="Card back">
    <p class="holder-name">Marissa Pendrell</p>
    <p class="holder-role">Life Coach</p>
    <ul class="contact-grid">
      <li class="contact-item">
        <svg viewBox="0 0 24 24" aria-hidden="true"><path fill="var(--ink)" d="M6.6 10.8a15.1 15.1 0 0 0 6.6 6.6l2.2-2.2c.3-.3.7-.4 1-.2 1.1.4 2.3.6 3.6.6.6 0 1 .4 1 1V20c0 .6-.4 1-1 1A17 17 0 0 1 3 4c0-.6.4-1 1-1h3.5c.6 0 1 .4 1 1 0 1.3.2 2.5.6 3.6.1.3 0 .7-.2 1z"/></svg>
        <span>518.677.3941</span>
      </li>
      <li class="contact-item">
        <svg viewBox="0 0 24 24" aria-hidden="true"><circle cx="12" cy="12" r="5" fill="none" stroke="var(--ink)" stroke-width="2.4"/><path fill="none" stroke="var(--ink)" stroke-width="2.4" stroke-linecap="round" d="M17 8v5.5a2.5 2.5 0 0 0 5 0V12a10 10 0 1 0-4 8"/></svg>
        <span>marissa@calmbriefcounsel.net</span>
      </li>
      <li class="contact-item">
        <svg viewBox="0 0 24 24" aria-hidden="true"><g fill="none" stroke="var(--ink)" stroke-width="1.8"><circle cx="12" cy="12" r="10"/><ellipse cx="12" cy="12" rx="4.5" ry="10"/><path d="M2 12h20M4 6.5h16M4 17.5h16"/></g></svg>
        <span>calmbriefcounsel.net</span>
      </li>
      <li class="contact-item">
        <svg viewBox="0 0 24 24" aria-hidden="true"><rect x="3" y="3" width="18" height="18" fill="var(--ink)"/></svg>
        <span>@calmbriefcounsel</span>
      </li>
    </ul>
  </section>
</main>
</body>
</html>
```